British Columbia Day banner showcasing 20% off site

Banner graphic promoting our BC Day sale
Size: 1800 x 1000
- flag has been uploaded for inspiration
- examples from other companies and their sale banners have been uploaded for inspiration.
- product images can be found at www.mygreenleafhub.com, please use a variety of different products in this banner

Target Market(s)

19+

Industry/Entity Type

Cannabis

Requirements
Must have
• Phrases:
- “Celebrate BC Day with BC bud and companies”
- “20% off site wide sale*"
- Underneath phrase the date of sale “July 30th - August 3rd”
- In tiny print “*excludes all sale and bundled items”
- MUST BE 1800 X1000
Nice to have
• - images of the products or bud we carry which can be found at www.mygreenleafhub.com
- bold
Should not have
• - company logo

```html
<!DOCTYPE html>
<html lang="en">
<head>
<meta charset="utf-8">
<title>BC Day Sale Banner</title>
<link rel="stylesheet" href="https://fonts.googleapis.com/css2?family=Russo+One&family=Exo+2:wght@500;600&display=swap">
<style>
  :root {
    --leaf-green: #8dc63f;
    --leaf-green-soft: #c4e39a;
    --ink: #111111;
    --paper: #ffffff;
  }
  * { margin: 0; padding: 0; box-sizing: border-box; }
  html, body { width: 1200px; height: 670px; overflow: hidden; background: var(--paper); }
  .banner {
    position: relative;
    width: 1200px;
    height: 670px;
    background: var(--paper);
    overflow: hidden;
    font-family: "Exo 2", sans-serif;
    color: var(--ink);
  }
  .brand {
    position: absolute;
    left: 75px;
    top: 140px;
    display: flex;
    align-items: center;
    gap: 12px;
    font-weight: 600;
    font-size: 36px;
    line-height: 1;
    color: var(--ink);
  }
  .brand-mark {
    width: 26px;
    height: 26px;
    background: var(--leaf-green);
  }
  .discount {
    position: absolute;
    left: 70px;
    top: 292px;
    font-family: "Russo One", sans-serif;
    font-size: 138px;
    line-height: 1;
    color: var(--leaf-green);
  }
  .sale-line {
    position: absolute;
    left: 70px;
    top: 438px;
    font-family: "Russo One", sans-serif;
    font-size: 56px;
    line-height: 1;
    letter-spacing: 1px;
    word-spacing: 8px;
    white-space: nowrap;
  }
  .sale-dates {
    position: absolute;
    left: 72px;
    top: 530px;
    font-weight: 500;
    font-size: 42px;
    line-height: 1;
    white-space: nowrap;
  }
  .fine-print {
    position: absolute;
    left: 552px;
    top: 562px;
    font-weight: 500;
    font-size: 20px;
    line-height: 1;
    letter-spacing: 7.3px;
    white-space: nowrap;
  }
  .feature-shape {
    position: absolute;
    left: 527px;
    top: 0;
    width: 644px;
    height: 515px;
    background: var(--ink);
    clip-path: polygon(50.3% 0, 100% 65.2%, 50.3% 100%, 0 65.2%);
  }
  .headline {
    position: absolute;
    left: 646px;
    top: 261px;
    width: 400px;
    text-align: center;
    font-weight: 600;
    font-size: 42px;
    line-height: 51px;
    color: var(--leaf-green);
    white-space: nowrap;
  }
  .leaf-border {
    position: absolute;
    left: 0;
    bottom: 0;
    width: 1200px;
    height: 68px;
    background: linear-gradient(to bottom, var(--paper), var(--leaf-green-soft) 45%, var(--leaf-green));
  }
</style>
</head>
<body>
  <main class="banner">
    <div class="feature-shape" role="img" aria-label="Large black maple leaf behind the headline"></div>

    <div class="brand"><span class="brand-mark"></span><span class="brand-name">Green Leaf Hub</span></div>

    <p class="discount">20%</p>
    <p class="sale-line">off site wide sale*</p>
    <p class="sale-dates">July 30th - August 3rd</p>

    <p class="headline">Celebrate BC Day<br>with BC bud<br>and companies</p>

    <p class="fine-print">*excludes all sale and bundled items</p>

    <div class="leaf-border" role="img" aria-label="Row of green leaf shapes along the bottom edge"></div>
  </main>
</body>
</html>
```